BWR Brochure Design Project

Bluewater Ridge MaintenanceChanges needed to attached flyer...Contact should be Customer Service instead of Customer Service.Contact number is 216-555-0193.Cleaning pictures welcome from carpet cleaning, vacuuming floors, mopping, Staff cleaning office environment (not homes). Multi-cultural staff pictures. We currently clean in 18 states around the USA. We DO NOT do screen cleaning or parking lot striping. We do everything else listed in the flyer. The map is incorrect.... we service AR CA CO FL IA IN KY KS LA MA MD MI MN MO NJ OH PA SD TX WV VA.

Address
4820 Willowmere Ave East
Suite 2300
Cleveland, Ohio 44187

Target Market(s)

Movie Theaters and Entertainment Venues

Industry/Entity Type

Cleaning Service

Requirements
Must have
• A NEW MAP.
• New Pictures

```html
<!DOCTYPE html>
<html lang="en">
<head>
<meta charset="utf-8">
<title>Bluewater Ridge Maintenance – Theatre Cleaning Brochure</title>
<link rel="stylesheet" href="https://fonts.googleapis.com/css2?family=Cinzel:wght@400;600&family=Raleway:wght@400;600;700&family=Roboto+Condensed:wght@400;700&display=swap">
<style>
:root{
  --green:#8cc07c;
  --green-dark:#6fa862;
  --green-light:#a9d49a;
  --ink:#161616;
  --text:#2a2a2a;
  --paper:#f4f4f4;
  --paper-shade:#e4e4e4;
  --stage:#8a8a8a;
  --seat-red:#b3261e;
}
*{box-sizing:border-box;margin:0;padding:0}
html,body{width:829px;height:1200px;overflow:hidden}
body{background:var(--stage);font-family:"Raleway",sans-serif;color:var(--text);position:relative}
.sheet{position:absolute;left:74px;width:683px;background:linear-gradient(90deg,var(--paper) 0%,#fff 30%,var(--paper-shade) 33%,#fff 36%,#fafafa 64%,var(--paper-shade) 66.5%,#fff 69%,#f6f6f6 100%);overflow:hidden;box-shadow:0 2px 10px rgba(0,0,0,.35)}
.sheet--outside{top:62px;height:528px}
.sheet--inside{top:610px;height:526px}
.abs{position:absolute}
.bands{position:absolute;inset:0;width:100%;height:100%}
.photo{position:absolute}
.brand-name{font-family:"Cinzel",serif;font-weight:400;color:var(--green);white-space:nowrap}
.brand-name--dark{color:var(--ink)}

/* outside: cover */
.cover-brand{left:476px;top:78px;font-size:15px;line-height:1.1;display:flex;align-items:center;gap:8px}
.cover-brand .mark{width:14px;height:14px;background:var(--ink);flex:none}
.headline{left:476px;top:136px;width:186px;text-align:center;font-weight:400}
.headline .serif{font-family:"Cinzel",serif;font-size:33px;line-height:1;letter-spacing:-.5px}
.headline .experts{color:var(--green)}
.headline .cleaning{color:var(--ink);margin-top:2px}
.headline .rule{display:flex;align-items:center;gap:6px;font-family:"Roboto Condensed",sans-serif;font-weight:700;font-size:17px;color:var(--ink);margin:2px 0}
.headline .rule::before,.headline .rule::after{content:"";flex:1;height:1.5px;background:var(--ink)}
.headline .theatres{font-family:"Roboto Condensed",sans-serif;font-weight:700;font-size:42px;color:var(--green);line-height:1;letter-spacing:.5px}
.headline .venues{font-family:"Roboto Condensed",sans-serif;font-size:16px;color:var(--green);letter-spacing:.3px}

/* outside: back panel */
.back-brand{left:228px;top:130px;width:222px;text-align:center;font-size:22px;line-height:1.2}
.address{left:228px;top:256px;width:222px;text-align:center;font-size:9.5px;line-height:1.6;color:var(--ink)}
.address strong{font-weight:700}

.call-box{left:506px;top:442px;width:132px;height:60px;border:1.5px solid var(--ink);border-radius:4px;text-align:center;color:var(--ink)}
.call-box::after{content:"";position:absolute;inset:3px;border:1px solid var(--ink);border-radius:2px}
.call-box .phone-icon{position:absolute;left:57px;top:-12px;width:18px;height:18px;border-radius:50%;background:var(--green);border:1.5px solid var(--ink)}
.call-box .call{font-family:"Roboto Condensed",sans-serif;font-weight:700;font-size:23px;line-height:1;margin-top:10px}
.call-box .num{font-family:"Roboto Condensed",sans-serif;font-weight:700;font-size:14px}

/* inside */
.inside-brand{left:22px;top:28px;display:flex;align-items:center;gap:8px}
.inside-brand .mark{width:16px;height:16px;background:var(--ink);flex:none}
.inside-brand .brand-name{color:#fff;font-size:17px}
.intro{left:18px;top:120px;width:196px;font-size:10.2px;line-height:1.26;text-align:justify;color:var(--ink)}
.intro p+p{margin-top:12px}
.contact{left:8px;top:306px;width:212px;text-align:center}
.contact h3{font-family:"Roboto Condensed",sans-serif;font-weight:400;color:var(--green);font-size:14.5px;line-height:1.06;letter-spacing:.2px}
.contact p{font-size:10px;line-height:1.32;color:var(--ink)}
.contact b{font-weight:700}

.section-head{font-family:"Raleway",sans-serif;font-size:13.5px;line-height:1.06;color:var(--green);font-weight:400;text-transform:uppercase;letter-spacing:-.2px}
.section-head b{font-weight:700}
.states-head{left:248px;top:84px;width:196px;padding-bottom:4px;border-bottom:1.2px solid var(--ink)}
.services-head{left:478px;top:42px;width:186px;padding-bottom:4px;border-bottom:1.2px solid var(--ink)}

.checklist{list-style:none;font-size:10.3px;color:var(--ink);line-height:15.9px}
.checklist li{position:relative;padding-left:15px;white-space:nowrap}
.checklist li::before{content:"";position:absolute;left:0;top:4px;width:7px;height:7px;border:1px solid var(--green)}
.checklist li::after{content:"";position:absolute;left:2px;top:3px;width:3px;height:6px;border:solid var(--green-dark);border-width:0 1.5px 1.5px 0;transform:rotate(40deg)}
.states-a{left:248px;top:126px}
.states-b{left:338px;top:126px}
.services{left:478px;top:116px}

.coming{left:240px;top:430px;width:212px;text-align:center;font-size:13px;line-height:1.1;color:var(--green)}
.coming b{font-weight:700}

.callout{left:500px;top:292px;width:140px;height:60px;background:var(--green);border-radius:6px;transform:rotate(-8deg);color:var(--ink);font-size:9.5px;line-height:1.25;text-align:center;padding:9px 8px}
.callout b{font-weight:700}
.callout-pin{left:545px;top:262px;width:0;height:32px;border-left:1px solid var(--ink);transform:rotate(40deg);transform-origin:top}

.web{left:455px;top:486px;width:228px;text-align:center;font-size:11px;color:#fff;letter-spacing:.6px}
</style>
</head>
<body>

<!-- Outside spread: back flap, back cover, front cover -->
<section class="sheet sheet--outside" aria-label="Brochure outside spread">
  <div class="photo" style="left:0;top:40px;width:224px;height:150px;background:linear-gradient(160deg,#c9a77a 0%,#b9b2a8 45%,#8e9196 100%)" role="img" aria-label="Photo: restroom sink counter being cleaned with a vacuum wand"></div>
  <div class="photo" style="left:0;top:190px;width:224px;height:48px;background:linear-gradient(180deg,#8e9196,#4a3c36)" role="img" aria-label="Photo: vacuum nozzle on carpet"></div>
  <div class="photo" style="left:0;top:238px;width:224px;height:138px;background:linear-gradient(165deg,#3a1612 0%,var(--seat-red) 50%,#5a1b15 100%)" role="img" aria-label="Photo: row of red theatre seats"></div>
  <div class="photo" style="left:0;top:376px;width:224px;height:110px;background:linear-gradient(150deg,#9c9a96 0%,#c4c2bd 55%,#8b8985 100%)" role="img" aria-label="Photo: pressure washer spraying a concrete floor"></div>
  <div class="photo" style="left:224px;top:360px;width:459px;height:125px;background:linear-gradient(180deg,#f1f1f1 0%,#5a1a16 22%,var(--seat-red) 55%,#2a0d0b 100%)" role="img" aria-label="Photo: empty auditorium with rows of red theatre seats"></div>

  <svg class="bands" viewBox="0 0 683 528" preserveAspectRatio="none" aria-hidden="true">
    <polygon points="0,0 640,0 224,56 0,56" fill="#8cc07c"/>
    <polygon points="224,0 640,0 300,48 224,54" fill="#9ccb8c"/>
    <polygon points="450,14 683,0 683,4 520,14" fill="#161616"/>
    <polygon points="0,466 224,440 683,440 683,528 0,528" fill="#161616"/>
    <polygon points="330,480 683,418 683,528 520,528" fill="#8cc07c"/>
    <polygon points="250,486 560,460 683,480 683,486" fill="#6fa862" opacity=".5"/>
  </svg>

  <div class="abs back-brand"><span class="brand-name brand-name--dark">Bluewater Ridge</span></div>
  <p class="abs address">4820 Willowmere Avenue<br>East Suite 2300<br>Cleveland, OH 44187<br><strong>216.555.0193</strong></p>

  <div class="abs cover-brand"><span class="mark"></span><span class="brand-name">Bluewater Ridge</span></div>
  <h1 class="abs headline">
    <div class="serif experts">EXPERTS</div>
    <div class="rule">IN</div>
    <div class="serif cleaning">CLEANING</div>
    <div class="theatres">THEATRES</div>
    <div class="rule">AND</div>
    <div class="venues">ENTERTAINMENT VENUES</div>
  </h1>

  <div class="abs call-box">
    <span class="phone-icon"></span>
    <div class="call">CALL US!</div>
    <div class="num">216.555.0193</div>
  </div>
</section>

<!-- Inside spread: intro, states, services -->
<section class="sheet sheet--inside" aria-label="Brochure inside spread">
  <div class="photo" style="left:0;top:398px;width:228px;height:110px;background:linear-gradient(160deg,#2a0d0b 0%,var(--seat-red) 45%,#3a1612 100%)" role="img" aria-label="Photo: staff member cleaning between rows of red theatre seats"></div>
  <div class="photo" style="left:248px;top:308px;width:196px;height:116px;background:radial-gradient(ellipse at 60% 55%,var(--green) 0%,#b9c9b0 55%,#c8c8c8 80%,transparent 100%)" role="img" aria-label="Map of the United States with served states highlighted in green"></div>
  <div class="photo" style="left:470px;top:376px;width:200px;height:84px;background:linear-gradient(180deg,#f3f3f3 0%,#d8d8d8 60%,#6b6b6b 100%);border-radius:10px 30px 8px 8px" role="img" aria-label="Photo: white company service van"></div>

  <svg class="bands" viewBox="0 0 683 526" preserveAspectRatio="none" aria-hidden="true">
    <polygon points="0,0 228,0 228,82 0,100" fill="#8cc07c"/>
    <polygon points="228,0 455,0 455,44 228,82" fill="#9ccb8c"/>
    <polygon points="455,0 683,0 683,6 455,44" fill="#a9d49a"/>
    <polygon points="0,100 683,2 683,16 0,112" fill="#161616"/>
    <polygon points="230,492 683,420 683,460" fill="#8cc07c"/>
    <polygon points="0,504 683,458 683,526 0,526" fill="#161616"/>
  </svg>

  <div class="abs inside-brand"><span class="mark"></span><span class="brand-name">Bluewater Ridge</span></div>

  <div class="abs intro">
    <p>At Bluewater Ridge, we treat each building with special care. Our job is to concentrate on the cleanliness of your building, lessening your workload and allowing you to concentrate on the many demands of running your business.</p>
    <p>We provide expert cleaning services seven days a week, 365 days a year. When you leave your facility each night, we give you peace of mind that your assets will be cared for and cleaned to the highest professional standards.</p>
  </div>

  <div class="abs contact">
    <h3>FOR MORE INFORMATION OR<br>TO OBTAIN A FREE QUOTE,<br>PLEASE CONTACT:</h3>
    <p><b>Customer Service</b><br>216.555.0193<br>service@bluewaterridgeclean.com</p>
  </div>

  <h2 class="abs section-head states-head">We <b>currently</b><br><b>serve</b> theatres in:</h2>
  <ul class="abs checklist states-a">
    <li>Arkansas</li><li>California</li><li>Colorado</li><li>Florida</li><li>Indiana</li><li>Iowa</li><li>Kansas</li><li>Kentucky</li><li>Louisiana</li><li>Maryland</li><li>Massachusetts</li>
  </ul>
  <ul class="abs checklist states-b">
    <li>Michigan</li><li>Minnesota</li><li>Missouri</li><li>New Jersey</li><li>Ohio</li><li>Pennsylvania</li><li>South Dakota</li><li>Texas</li><li>Virginia</li><li>West Virginia</li>
  </ul>
  <p class="abs coming"><b>COMING</b> TO YOUR<br>STATE <b>SOON!</b></p>

  <h2 class="abs section-head services-head">In addition to <b>nightly</b><br>janitorial, <b>we offer</b><br>the following<br><b>professional</b> services:</h2>
  <ul class="abs checklist services">
    <li>Carpet Cleaning</li><li>Seat Cleaning</li><li>Tile and Marble</li><li>Pressure Washing</li><li>Stripping and Waxing Floors</li><li>High Dusting</li><li>Sound Fold Cleaning</li><li>Window Washing</li>
  </ul>

  <span class="abs callout-pin" aria-hidden="true"></span>
  <p class="abs callout">Our <b>aquasurge truck Mount system</b> ensures maximum heat and extraction power.</p>

  <p class="abs web">www.bluewaterridgeclean.com</p>
</section>

</body>
</html>
```